Delivery Performance Dashboard for Web Portal

We need you to design a dashboard for our web portal. We deliver sand and stone to construction jobsites. The attached screenshot is from our current web portal dashboard . It shows how much material has been delivered from an order.

HaulTrack will deliver multiple loads during the day and the dispatcher uses the dashboard to monitor if they need to add more trucks or less trucks to fulfill the order. An example would be, I need to ship 1,000 tons of sand to a jobsite and I plan to use 10 trucks during the day and that it will take 10 hours of hauling to complete the job. After 5 hours of hauling (50% the day is over), I should have delivered 500 tons of sand (50% of the order). But maybe there is a lot of traffic, and I only have delivered 300 tons. The dashboard will show that I am behind schedule and I might need to add 2 more trucks to the job.

Industry/Entity Type

Construction

Font styles to use
Sans Serif

Requirements
Must have
• We need a progress bar showing how much material has been delivered, how much material was requested to be delivered total and how much material should have been delivered at the current time. The goal is to show the user if the deliveries are ahead or behind the expected pace and why.
Nice to have
• The icons for plant, driving and jobsite show if the actual times have exceeded or beaten the planned times. Maybe you have other ideas to show the user if the trucks are sitting longer on the jobsite, at the plant to get loaded or driving to and from the jobsite.

```html
<!DOCTYPE html>
<html lang="en">
<head>
<meta charset="utf-8">
<title>HaulTrack – Delivery Performance</title>
<link href="https://fonts.googleapis.com/css2?family=Poppins:wght@400;500;600&family=Roboto:wght@400;500&display=swap" rel="stylesheet">
<style>
:root{
  --stage:#1d2c3b;
  --white:#ffffff;
  --page:#f1f4f8;
  --brand:#21479a;
  --side:#2b539f;
  --side-active:#4a90e2;
  --head-top:#2f7ee0;
  --head-bottom:#1a5fc2;
  --ink:#3a3f47;
  --muted:#6b7280;
  --line:#e6e9ee;
  --row-alt:#f6f7f9;
  --bar:#1a64d0;
  --ahead:#7cb342;
  --behind:#e6541c;
  --ontime:#1e5bb0;
}
*{box-sizing:border-box;margin:0;padding:0}
html,body{width:928px;height:1200px;overflow:hidden}
body{background:var(--stage);font-family:"Roboto",sans-serif;color:var(--ink);position:relative}
.screen{position:absolute;left:65px;width:797px;height:498px;background:var(--page);overflow:hidden}
.screen--list{top:85px}
.screen--detail{top:616px}
.topbar{position:absolute;left:0;top:0;width:100%;height:35px;background:var(--white);border-bottom:1px solid var(--line)}
.brand{position:absolute;left:16px;top:5px;font-family:"Poppins",sans-serif;font-weight:600;font-size:15px;line-height:22px;color:var(--brand);letter-spacing:.3px}
.user-nav{position:absolute;right:38px;top:10px;display:flex;align-items:center;gap:16px;font-family:"Poppins",sans-serif;font-size:6.3px}
.user{display:flex;align-items:center;gap:6px;font-weight:600;font-size:5px;color:#222}
.avatar{width:16px;height:16px;border-radius:50%;background:linear-gradient(135deg,#8aa3bd,#3f5a78)}
.nav-link{display:flex;align-items:center;gap:4px;color:#555}
.nav-link svg{width:8px;height:8px}
.sidebar{position:absolute;left:0;top:35px;width:32px;bottom:0;background:var(--side)}
.side-item{height:32px;border-bottom:1px solid rgba(255,255,255,.12);display:flex;align-items:center;justify-content:center}
.side-item--active{background:var(--side-active)}
.side-item svg{width:9px;height:9px;fill:var(--white)}
.orders{position:absolute;left:64px;top:59px;width:702px;height:342px;background:var(--white);box-shadow:0 0 2px rgba(0,0,0,.12)}
.grid{display:grid;grid-template-columns:44px 79px 97px 120px 55px 135px 81px 49px 42px}
.orders-head{height:27px;background:linear-gradient(var(--head-top),var(--head-bottom));color:var(--white);font-family:"Poppins",sans-serif;font-weight:500;font-size:5.2px;align-items:center}
.orders-head span{padding-left:13px;display:flex;align-items:center;gap:3px}
.orders-head .c-wait{padding-left:14px}
.orders-head svg{width:6px;height:6px;stroke:#fff;fill:none}
.row{height:39.5px;font-size:5.2px;align-items:stretch}
.row:nth-child(odd){background:var(--row-alt)}
.row>div{display:flex;align-items:center;padding-left:13px;border-right:1px solid var(--line)}
.row>div:last-child{border-right:0}
.c-order{font-size:5.6px}
.progress{flex-direction:column;align-items:flex-start!important;justify-content:center;padding-left:21px!important}
.bar{width:99px;height:3px;border:.6px solid var(--bar);border-radius:2px;overflow:hidden}
.bar i{display:block;width:58%;height:100%;background:var(--bar)}
.bar-meta{width:99px;display:flex;justify-content:space-between;margin-top:3px;font-size:4.5px}
.waits{padding-left:0!important;display:grid!important;grid-template-columns:28px 22px 31px}
.wait{display:flex;align-items:center;justify-content:center;gap:2px;height:100%;border-right:1px solid var(--line)}
.wait:last-child{border-right:0}
.wait svg{width:7px;height:7px;stroke:#6a7280;fill:none;stroke-width:1.2}
.caret{width:0;height:0;border-left:1.6px solid transparent;border-right:1.6px solid transparent;border-top:2px solid #444}
.rem{font-weight:500;font-size:5.2px}
.ahead{color:var(--ahead)}.behind{color:var(--behind)}.ontime{color:var(--ontime)}
.delta{font-weight:500;font-size:5.4px;padding-left:13px}
.pager{position:absolute;left:289px;top:294px;display:flex;gap:3px;align-items:flex-end}
.pager span{width:12px;height:12px;border:1px solid #cfd4db;font-size:5px;display:flex;align-items:center;justify-content:center;background:#fff}
.pager .arrow{background:#b7bcc3;border-color:#b7bcc3}
.pager .arrow svg{width:4px;height:4px;fill:#fff}
.pager .dots{border:0;width:6px;background:none;align-items:flex-end}
.footer-rule{position:absolute;left:64px;right:31px;top:439px;border-top:1px solid #dde2e8}
.footer{position:absolute;left:0;right:0;top:461px;text-align:center;font-family:"Poppins",sans-serif;font-size:5.3px;color:#333;padding-left:32px}
.cycle-card{position:absolute;left:607px;top:116px;width:121px;height:168px;background:var(--white);box-shadow:0 2px 6px rgba(0,0,0,.25);font-size:4.4px}
.cycle-card h3{height:15px;background:var(--head-bottom);color:#fff;font-family:"Poppins",sans-serif;font-weight:400;font-size:5.6px;display:flex;align-items:center;justify-content:center}
.cycle-avg{height:20px;display:flex;align-items:center;justify-content:space-between;padding:0 9px;border-bottom:1px solid var(--line)}
.cycle-avg svg{width:16px;height:8px;stroke:var(--bar);fill:none}
.stage{height:35px;padding:5px 9px 0;border-bottom:1px solid var(--line)}
.stage:last-child{border-bottom:0}
.stage-title{display:flex;align-items:center;gap:4px;font-family:"Poppins",sans-serif;font-weight:500;font-size:4.6px}
.stage-title svg{width:12px;height:12px;stroke:var(--bar);fill:none;stroke-width:1}
.stage-vals{display:flex;justify-content:space-between;margin-top:5px}
</style>
</head>
<body>
<svg width="0" height="0" style="position:absolute">
  <symbol id="i-plant" viewBox="0 0 12 12"><path d="M1 11h10M2 11V6l3-2v2l3-2v7M9 11V2h1.5v9"/></symbol>
  <symbol id="i-truck" viewBox="0 0 12 12"><path d="M1 3h6v5H1zM7 5h2.5l1.5 2v1H7"/><circle cx="3" cy="9" r="1.2"/><circle cx="9" cy="9" r="1.2"/></symbol>
  <symbol id="i-pin" viewBox="0 0 12 12"><path d="M6 11S2.5 7 2.5 4.5a3.5 3.5 0 017 0C9.5 7 6 11 6 11z"/><circle cx="6" cy="4.5" r="1.2"/></symbol>
  <symbol id="i-dig" viewBox="0 0 12 12"><path d="M1 10h6V6H1zM7 8l2-5 2 2M2 10v1M6 10v1"/></symbol>
  <symbol id="s-grid" viewBox="0 0 10 10"><g><rect x="0" y="1" width="2" height="2"/><rect x="3" y="1" width="2" height="2"/><rect x="6" y="1" width="2" height="2"/><rect x="9" y="1" width="1" height="2"/><rect x="0" y="4" width="2" height="2"/><rect x="3" y="4" width="2" height="2"/><rect x="6" y="4" width="2" height="2"/><rect x="9" y="4" width="1" height="2"/><rect x="0" y="7" width="2" height="2"/><rect x="3" y="7" width="2" height="2"/><rect x="6" y="7" width="2" height="2"/><rect x="9" y="7" width="1" height="2"/></g></symbol>
  <symbol id="s-doc" viewBox="0 0 10 10"><path d="M2 0h4l3 3v7H2z"/></symbol>
  <symbol id="s-stack" viewBox="0 0 10 10"><path d="M1 4h6v5H1zM3 1h6v5H8V2H3z"/></symbol>
  <symbol id="s-feed" viewBox="0 0 10 10"><circle cx="2" cy="8" r="1.3"/><path d="M1 4a5 5 0 015 5H5a4 4 0 00-4-4zM1 1a8 8 0 018 8H8a7 7 0 00-7-7z"/></symbol>
  <symbol id="s-window" viewBox="0 0 10 10"><path d="M1 2h8v7H1zm1 2v4h6V4z"/></symbol>
  <symbol id="s-list" viewBox="0 0 10 10"><path d="M1 2h1v1H1zM3 2h6v1H3zM1 5h1v1H1zM3 5h6v1H3zM1 8h1v1H1zM3 8h6v1H3z"/></symbol>
  <symbol id="s-chat" viewBox="0 0 10 10"><path d="M1 1h8v6H4L2 9V7H1zm2 2v1h4V3zm0 2v1h3V5z"/></symbol>
  <symbol id="s-image" viewBox="0 0 10 10"><path d="M1 1h8v8H1zm1 6h6L6 4 4 6 3 5z"/></symbol>
  <symbol id="s-pages" viewBox="0 0 10 10"><path d="M3 0h7v8H3zM0 2h2v7h6v1H0zM4 2v1h5V2zm0 2v1h5V4z" fill-rule="evenodd"/></symbol>
  <symbol id="s-tiles" viewBox="0 0 10 10"><path d="M1 1h3v4H1zM5 1h4v2H5zM5 4h4v5H5zM1 6h3v3H1z"/></symbol>
  <symbol id="s-note" viewBox="0 0 10 10"><path d="M1 1h8v8H1zm2 2v1h4V3zm0 2v1h4V5zm0 2v1h4V7z" fill-rule="evenodd"/></symbol>
</svg>

<!-- Orders list screen -->
<section class="screen screen--list">
  <header class="topbar">
    <div class="brand">HaulTrack</div>
    <nav class="user-nav">
      <div class="user"><div class="avatar" role="img" aria-label="User profile photo"></div>Dana Whitfield</div>
      <div class="nav-link"><svg viewBox="0 0 10 10" fill="none" stroke="#777"><circle cx="5" cy="5" r="3.5"/><circle cx="5" cy="5" r="1.3"/></svg>Settings</div>
      <div class="nav-link"><svg viewBox="0 0 10 10" fill="none" stroke="#777"><rect x="1" y="1" width="8" height="8" rx="1"/><path d="M3.5 3.5l3 3M6.5 3.5l-3 3"/></svg>Logout</div>
    </nav>
  </header>
  <aside class="sidebar">
    <div class="side-item"><svg><use href="#s-grid"/></svg></div>
    <div class="side-item side-item--active"><svg><use href="#s-doc"/></svg></div>
    <div class="side-item"><svg><use href="#s-stack"/></svg></div>
    <div class="side-item"><svg><use href="#s-feed"/></svg></div>
    <div class="side-item"><svg><use href="#s-window"/></svg></div>
    <div class="side-item"><svg><use href="#s-list"/></svg></div>
    <div class="side-item"><svg><use href="#s-chat"/></svg></div>
    <div class="side-item"><svg><use href="#s-image"/></svg></div>
    <div class="side-item"><svg><use href="#s-pages"/></svg></div>
    <div class="side-item"><svg><use href="#s-tiles"/></svg></div>
    <div class="side-item"><svg><use href="#s-note"/></svg></div>
    <div class="side-item"></div>
  </aside>
  <main class="orders">
    <div class="grid orders-head">
      <span>Order</span><span>Origin</span><span>Destination</span><span>Customer</span><span>Status</span><span>Tons</span><span class="c-wait">Wait Times</span><span>Remaining <svg viewBox="0 0 10 10"><circle cx="5" cy="5" r="4"/><path d="M5 2.5V5l2 1"/></svg></span><span>+/- <svg viewBox="0 0 12 12"><use href="#i-truck"/></svg></span>
    </div>
    <div class="rows">
      <div class="grid row"><div class="c-order">17746</div><div>Ridgeway Asphalt Plant</div><div>KTJV -185 from mm 77 - 98</div><div>Harlan Construction - North Division</div><div>Accepted</div><div class="progress"><div class="bar"><i></i></div><div class="bar-meta"><span>722.57 / 1500</span><span>7:30am - 5:00pm</span></div></div><div class="waits"><span class="wait"><svg><use href="#i-plant"/></svg><b class="caret"></b></span><span class="wait"><svg><use href="#i-truck"/></svg><b class="caret"></b></span><span class="wait"><svg><use href="#i-pin"/></svg><b class="caret"></b></span></div><div class="rem ahead">+1:25 hrs</div><div class="delta">-31</div></div>
      <div class="grid row"><div class="c-order">17746</div><div>Marlow Asphalt</div><div>Cedar Springs</div><div>Harlan Construction - North Division</div><div>Accepted</div><div class="progress"><div class="bar"><i></i></div><div class="bar-meta"><span>722.57 / 1500</span><span>7:30am - 5:00pm</span></div></div><div class="waits"><span class="wait"><svg><use href="#i-plant"/></svg><b class="caret"></b></span><span class="wait"><svg><use href="#i-truck"/></svg><b class="caret"></b></span><span class="wait"><svg><use href="#i-pin"/></svg><b class="caret"></b></span></div><div class="rem behind">-0:28 hrs</div><div class="delta">+16</div></div>
      <div class="grid row"><div class="c-order">17746</div><div>Ridgeway Asphalt Plant</div><div>KTJV -185 from mm 77 - 98</div><div>Harlan Construction - North Division</div><div>Accepted</div><div class="progress"><div class="bar"><i></i></div><div class="bar-meta"><span>722.57 / 1500</span><span>7:30am - 5:00pm</span></div></div><div class="waits"><span class="wait"><svg><use href="#i-plant"/></svg><b class="caret"></b></span><span class="wait"><svg><use href="#i-truck"/></svg><b class="caret"></b></span><span class="wait"><svg><use href="#i-pin"/></svg><b class="caret"></b></span></div><div class="rem ontime">8:00 hrs</div><div class="delta">-31</div></div>
      <div class="grid row"><div class="c-order">17746</div><div>Marlow Asphalt</div><div>Cedar Springs</div><div>Harlan Construction - North Division</div><div>Accepted</div><div class="progress"><div class="bar"><i></i></div><div class="bar-meta"><span>722.57 / 1500</span><span>7:30am - 5:00pm</span></div></div><div class="waits"><span class="wait"><svg><use href="#i-plant"/></svg><b class="caret"></b></span><span class="wait"><svg><use href="#i-truck"/></svg><b class="caret"></b></span><span class="wait"><svg><use href="#i-pin"/></svg><b class="caret"></b></span></div><div class="rem behind">-0:28 hrs</div><div class="delta">+16</div></div>
      <div class="grid row"><div class="c-order">17746</div><div>Ridgeway Asphalt Plant</div><div>KTJV -185 from mm 77 - 98</div><div>Harlan Construction - North Division</div><div>Accepted</div><div class="progress"><div class="bar"><i></i></div><div class="bar-meta"><span>722.57 / 1500</span><span>7:30am - 5:00pm</span></div></div><div class="waits"><span class="wait"><svg><use href="#i-plant"/></svg><b class="caret"></b></span><span class="wait"><svg><use href="#i-truck"/></svg><b class="caret"></b></span><span class="wait"><svg><use href="#i-pin"/></svg><b class="caret"></b></span></div><div class="rem ahead">+1:25 hrs</div><div class="delta">-31</div></div>
      <div class="grid row"><div class="c-order">17746</div><div>Marlow Asphalt</div><div>Cedar Springs</div><div>Harlan Construction - North Division</div><div>Accepted</div><div class="progress"><div class="bar"><i></i></div><div class="bar-meta"><span>722.57 / 1500</span><span>7:30am - 5:00pm</span></div></div><div class="waits"><span class="wait"><svg><use href="#i-plant"/></svg><b class="caret"></b></span><span class="wait"><svg><use href="#i-truck"/></svg><b class="caret"></b></span><span class="wait"><svg><use href="#i-pin"/></svg><b class="caret"></b></span></div><div class="rem ontime">8:00 hrs</div><div class="delta">+16</div></div>
    </div>
    <nav class="pager">
      <span class="arrow"><svg viewBox="0 0 4 4"><path d="M3 0v4L0 2z"/></svg></span><span>1</span><span>2</span><span>3</span><span>4</span><span>5</span><span class="dots">...</span><span>10</span><span class="arrow"><svg viewBox="0 0 4 4"><path d="M1 0v4l3-2z"/></svg></span>
    </nav>
  </main>
  <div class="footer-rule"></div>
  <footer class="footer">©2020 HaulTrack, All Rights Reserved.</footer>
</section>

<!-- Orders list with cycle detail -->
<section class="screen screen--detail">
  <header class="topbar">
    <div class="brand">HaulTrack</div>
    <nav class="user-nav">
      <div class="user"><div class="avatar" role="img" aria-label="User profile photo"></div>Dana Whitfield</div>
      <div class="nav-link"><svg viewBox="0 0 10 10" fill="none" stroke="#777"><circle cx="5" cy="5" r="3.5"/><circle cx="5" cy="5" r="1.3"/></svg>Settings</div>
      <div class="nav-link"><svg viewBox="0 0 10 10" fill="none" stroke="#777"><rect x="1" y="1" width="8" height="8" rx="1"/><path d="M3.5 3.5l3 3M6.5 3.5l-3 3"/></svg>Logout</div>
    </nav>
  </header>
  <aside class="sidebar">
    <div class="side-item"><svg><use href="#s-grid"/></svg></div>
    <div class="side-item side-item--active"><svg><use href="#s-doc"/></svg></div>
    <div class="side-item"><svg><use href="#s-stack"/></svg></div>
    <div class="side-item"><svg><use href="#s-feed"/></svg></div>
    <div class="side-item"><svg><use href="#s-window"/></svg></div>
    <div class="side-item"><svg><use href="#s-list"/></svg></div>
    <div class="side-item"><svg><use href="#s-chat"/></svg></div>
    <div class="side-item"><svg><use href="#s-image"/></svg></div>
    <div class="side-item"><svg><use href="#s-pages"/></svg></div>
    <div class="side-item"><svg><use href="#s-tiles"/></svg></div>
    <div class="side-item"><svg><use href="#s-note"/></svg></div>
    <div class="side-item"></div>
  </aside>
  <main class="orders">
    <div class="grid orders-head">
      <span>Order</span><span>Origin</span><span>Destination</span><span>Customer</span><span>Status</span><span>Tons</span><span class="c-wait">Wait Times</span><span>Remaining <svg viewBox="0 0 10 10"><circle cx="5" cy="5" r="4"/><path d="M5 2.5V5l2 1"/></svg></span><span>+/- <svg viewBox="0 0 12 12"><use href="#i-truck"/></svg></span>
    </div>
    <div class="rows">
      <div class="grid row"><div class="c-order">17746</div><div>Ridgeway Asphalt Plant</div><div>KTJV -185 from mm 77 - 98</div><div>Harlan Construction - North Division</div><div>Accepted</div><div class="progress"><div class="bar"><i></i></div><div class="bar-meta"><span>722.57 / 1500</span><span>7:30am - 5:00pm</span></div></div><div class="waits"><span class="wait"><svg><use href="#i-plant"/></svg><b class="caret"></b></span><span class="wait"><svg><use href="#i-truck"/></svg><b class="caret"></b></span><span class="wait"><svg><use href="#i-pin"/></svg><b class="caret"></b></span></div><div class="rem ahead">+1:25 hrs</div><div class="delta">-31</div></div>
      <div class="grid row"><div class="c-order">17746</div><div>Marlow Asphalt</div><div>Cedar Springs</div><div>Harlan Construction - North Division</div><div>Accepted</div><div class="progress"><div class="bar"><i></i></div><div class="bar-meta"><span>722.57 / 1500</span><span>7:30am - 5:00pm</span></div></div><div class="waits"><span class="wait"><svg><use href="#i-plant"/></svg><b class="caret"></b></span><span class="wait"><svg><use href="#i-truck"/></svg><b class="caret"></b></span><span class="wait"><svg><use href="#i-pin"/></svg><b class="caret"></b></span></div><div class="rem behind">-0:28 hrs</div><div class="delta">+16</div></div>
      <div class="grid row"><div class="c-order">17746</div><div>Ridgeway Asphalt Plant</div><div>KTJV -185 from mm 77 - 98</div><div>Harlan Construction - North Division</div><div>Accepted</div><div class="progress"><div class="bar"><i></i></div><div class="bar-meta"><span>722.57 / 1500</span><span>7:30am - 5:00pm</span></div></div><div class="waits"><span class="wait"><svg><use href="#i-plant"/></svg><b class="caret"></b></span><span class="wait"><svg><use href="#i-truck"/></svg><b class="caret"></b></span><span class="wait"><svg><use href="#i-pin"/></svg><b class="caret"></b></span></div><div class="rem ontime">8:00 hrs</div><div class="delta">-31</div></div>
      <div class="grid row"><div class="c-order">17746</div><div>Marlow Asphalt</div><div>Cedar Springs</div><div>Harlan Construction - North Division</div><div>Accepted</div><div class="progress"><div class="bar"><i></i></div><div class="bar-meta"><span>722.57 / 1500</span><span>7:30am - 5:00pm</span></div></div><div class="waits"><span class="wait"><svg><use href="#i-plant"/></svg><b class="caret"></b></span><span class="wait"><svg><use href="#i-truck"/></svg><b class="caret"></b></span><span class="wait"><svg><use href="#i-pin"/></svg><b class="caret"></b></span></div><div class="rem behind">-0:28 hrs</div><div class="delta">+16</div></div>
      <div class="grid row"><div class="c-order">17746</div><div>Ridgeway Asphalt Plant</div><div>KTJV -185 from mm 77 - 98</div><div>Harlan Construction - North Division</div><div>Accepted</div><div class="progress"><div class="bar"><i></i></div><div class="bar-meta"><span>722.57 / 1500</span><span>7:30am - 5:00pm</span></div></div><div class="waits"><span class="wait"><svg><use href="#i-plant"/></svg><b class="caret"></b></span><span class="wait"><svg><use href="#i-truck"/></svg><b class="caret"></b></span><span class="wait"><svg><use href="#i-pin"/></svg><b class="caret"></b></span></div><div class="rem ahead">+1:25 hrs</div><div class="delta">-31</div></div>
      <div class="grid row"><div class="c-order">17746</div><div>Marlow Asphalt</div><div>Cedar Springs</div><div>Harlan Construction - North Division</div><div>Accepted</div><div class="progress"><div class="bar"><i></i></div><div class="bar-meta"><span>722.57 / 1500</span><span>7:30am - 5:00pm</span></div></div><div class="waits"><span class="wait"><svg><use href="#i-plant"/></svg><b class="caret"></b></span><span class="wait"><svg><use href="#i-truck"/></svg><b class="caret"></b></span><span class="wait"><svg><use href="#i-pin"/></svg><b class="caret"></b></span></div><div class="rem ontime">8:00 hrs</div><div class="delta">+16</div></div>
    </div>
    <nav class="pager">
      <span class="arrow"><svg viewBox="0 0 4 4"><path d="M3 0v4L0 2z"/></svg></span><span>1</span><span>2</span><span>3</span><span>4</span><span>5</span><span class="dots">...</span><span>10</span><span class="arrow"><svg viewBox="0 0 4 4"><path d="M1 0v4l3-2z"/></svg></span>
    </nav>
  </main>
  <div class="cycle-card">
    <h3>Order 17746</h3>
    <div class="cycle-avg"><svg viewBox="0 0 16 8"><path d="M1 2.5h14M12 0.5l3 2M1 5.5h14M4 7.5l-3-2"/></svg><span>Avg Cycle Time: 2hr 27min</span></div>
    <div class="stage"><div class="stage-title"><svg viewBox="0 0 12 12"><use href="#i-plant"/></svg>Plant (min)</div><div class="stage-vals"><span>Planned: 30</span><span>Actual: 33</span></div></div>
    <div class="stage"><div class="stage-title"><svg viewBox="0 0 12 12"><use href="#i-truck"/></svg>Driving (min)</div><div class="stage-vals"><span>Planned: 60</span><span>Actual: 83</span></div></div>
    <div class="stage"><div class="stage-title"><svg viewBox="0 0 12 12"><use href="#i-pin"/></svg>Jobsite (min)</div><div class="stage-vals"><span>Planned: 30</span><span>Actual: 30</span></div></div>
    <div class="stage"><div class="stage-title"><svg viewBox="0 0 12 12"><use href="#i-dig"/></svg>Equipment (min)</div><div class="stage-vals"><span></span><span>Actual: -</span></div></div>
  </div>
  <div class="footer-rule"></div>
  <footer class="footer">©2020 HaulTrack, All Rights Reserved.</footer>
</section>
</body>
</html>
```